V STUDIO Interior & Exterior Designer Business needs a Business Card

V STUDIO - I need a Business Card Design for a Interior Design Business, I work Nationally Around Australia on Projects specialising In AGED CARE and would like to rebrand and change the Look.
I work mainly with Large Corporate Companys, Select everything From External Finishes to All Internal Finishes, Furniture and then Decorate to a 5 star finish.

Industry/Entity Type

Business

Contact Information for Business Card

V STUDIO
Marlena Hobart
PH: (+61) 0400 872 634
E: lenny@vstudiohub.example

Font styles to use
Sans Serif

Requirements
Must have
• My Priject Must Have a Contemporary Design, Bold, Eye Catching, that makes a statement but MUST BE ELEGANT - 2 or 3 Colours - Strong Power Colours.
• 2 sided
• i like the works - IMAGEN, DESIGN, CREATE
Nice to have
• I would like the words ' imagine design create ' incorporated into the design
• I like Some Red on the card

```html
<!DOCTYPE html>
<html lang="en">
<head>
<meta charset="utf-8">
<title>V STUDIO – Business Card</title>
<link rel="stylesheet" href="https://fonts.googleapis.com/css2?family=Cabin:wght@400;500;600;700&display=swap">
<style>
  :root {
    --backdrop: #d9d9dc;
    --paper: #ffffff;
    --navy: #2e3d63;
    --sky: #5b95d1;
    --signal-red: #cc2229;
    --gold: #c59f2d;
    --charcoal: #2b2c2f;
    --ink-black: #1d1d1f;
    --rule-blue: #3f5f9c;
    --text-light: #ffffff;
    --text-soft: #c9ccd3;
  }
  * { box-sizing: border-box; margin: 0; padding: 0; }
  html, body {
    width: 1200px; height: 954px; overflow: hidden;
    background: var(--backdrop);
    font-family: "Cabin", "Helvetica Neue", Arial, sans-serif;
  }
  .card {
    position: absolute; left: 75px; top: 177px;
    width: 1050px; height: 600px;
    background: var(--paper);
    overflow: hidden;
    box-shadow: 0 18px 40px rgba(0,0,0,.28);
  }
  .card__band { position: absolute; inset: 0; }
  .brand-block {
    position: absolute; left: 700px; top: 0; width: 350px; height: 200px;
    background: var(--ink-black);
    display: flex; flex-direction: column; align-items: center; justify-content: center;
    color: var(--text-light);
  }
  .brand-block__name { font-size: 46px; font-weight: 600; letter-spacing: 6px; }
  .brand-block__tagline { margin-top: 8px; font-size: 22px; font-weight: 400; color: var(--text-soft); letter-spacing: 1px; }
  .holder-name {
    position: absolute; left: 42px; top: 272px;
    font-size: 46px; font-weight: 600; color: var(--text-light);
  }
  .tile {
    position: absolute; color: var(--text-light);
    display: flex; flex-direction: column; align-items: center; justify-content: center;
    gap: 18px; font-size: 26px; font-weight: 500;
  }
  .tile svg { width: 46px; height: 46px; }
  .tile--email { left: 380px; top: 200px; width: 320px; height: 150px; background: var(--sky); font-size: 23px; }
  .tile--web { left: 700px; top: 200px; width: 350px; height: 150px; background: var(--signal-red); }
  .tile--phone { left: 0; top: 350px; width: 380px; height: 170px; background: var(--gold); }
  .footer-band {
    position: absolute; left: 0; top: 350px; width: 1050px; height: 250px;
    background: var(--charcoal);
  }
  .footer-band__rule {
    position: absolute; left: 410px; top: 40px; width: 600px; height: 2px;
    background: var(--rule-blue);
  }
  .address {
    position: absolute; left: 42px; top: 530px;
    font-size: 24px; line-height: 32px; color: var(--text-light);
  }
</style>
</head>
<body>
  <main class="card">
    <svg class="card__band" viewBox="0 0 1050 600" aria-hidden="true">
      <polygon points="0,250 520,165 1050,165 1050,600 0,600" fill="var(--navy)"/>
    </svg>

    <div class="brand-block">
      <span class="brand-block__name">V STUDIO</span>
      <span class="brand-block__tagline">Interior Designers</span>
    </div>

    <h1 class="holder-name">Marlena Hobart</h1>

    <div class="footer-band"><div class="footer-band__rule"></div></div>

    <div class="tile tile--email">
      <svg viewBox="0 0 48 48" aria-hidden="true">
        <rect x="4" y="11" width="40" height="27" fill="none" stroke="#fff" stroke-width="3"/>
        <polyline points="4,11 24,28 44,11" fill="none" stroke="#fff" stroke-width="3"/>
      </svg>
      <span>lenny@vstudiohub.example</span>
    </div>

    <div class="tile tile--web">
      <svg viewBox="0 0 48 48" aria-hidden="true" fill="none" stroke="#fff" stroke-width="3">
        <circle cx="24" cy="24" r="19"/>
        <ellipse cx="24" cy="24" rx="8" ry="19"/>
        <line x1="5" y1="24" x2="43" y2="24"/>
        <line x1="9" y1="14" x2="39" y2="14"/>
        <line x1="9" y1="34" x2="39" y2="34"/>
      </svg>
      <span>vstudiohub.example</span>
    </div>

    <div class="tile tile--phone">
      <svg viewBox="0 0 48 48" aria-hidden="true">
        <path d="M13 6 L20 14 L16 19 C19 26 22 29 29 32 L34 28 L42 35 L37 42 C22 41 7 26 6 11 Z" fill="#fff"/>
      </svg>
      <span>(+61) 0400 872 634</span>
    </div>

    <p class="address">Po box 4182, Marlowe Bay,<br>nsw 2391</p>
  </main>
</body>
</html>
```